We are in search of a new business card design for our business. We have a Mexican Grocery Store called Tortilla Grove Market, we would like to see that some have mexican design, but we are open to any type of designs.

Phone: to be announced
Fax: to be announced

Address is:
2415 Calloway Blvd
Dundalk, MD 21222

```html
<!DOCTYPE html>
<html lang="en">
<head>
<meta charset="utf-8">
<title>Tortilla Grove Market – Business Card</title>
<link rel="stylesheet" href="https://fonts.googleapis.com/css2?family=Open+Sans:wght@400;800&display=swap">
<style>
  :root {
    --page-bg: #e9e6e1;
    --card-light: #ffffff;
    --card-light-edge: #d9d9d9;
    --panel-dark: #3a3a3b;
    --panel-dark-deep: #2c2c2d;
    --accent-green: #2aa84a;
    --accent-red: #d8232a;
    --accent-red-deep: #7e1e1f;
    --icon-yellow: #ffc20e;
    --text-light: #ffffff;
    --brand-red: #c9202a;
  }
  * { margin: 0; padding: 0; box-sizing: border-box; }
  html, body {
    width: 1200px; height: 864px; overflow: hidden;
    background: var(--page-bg);
    font-family: "Open Sans", Arial, sans-serif;
  }
  .business-card {
    position: absolute; left: 80px; top: 122px;
    width: 1040px; height: 620px;
    overflow: hidden;
    box-shadow: 0 10px 26px rgba(0,0,0,.28);
  }
  .card-shapes { position: absolute; inset: 0; }
  .brand-name {
    position: absolute; left: 60px; top: 200px; width: 320px;
    text-align: center;
    font-weight: 800; font-size: 48px; line-height: 1.08;
    color: var(--brand-red);
  }
  .contact-list {
    position: absolute; right: 60px; top: 0;
    list-style: none;
  }
  .contact-item {
    position: absolute; right: 0;
    display: flex; align-items: center; gap: 22px;
    white-space: nowrap;
  }
  .contact-text {
    color: var(--text-light);
    font-size: 28px; line-height: 1.4; font-weight: 400;
    text-align: right;
  }
  .contact-icon {
    width: 60px; height: 60px; flex: none;
    border: 3px solid var(--text-light);
    display: flex; align-items: center; justify-content: center;
  }
  .contact-icon svg { width: 38px; height: 38px; }
  .item-address { top: 46px; }
  .item-email { top: 162px; }
  .item-phone { top: 266px; }
  .item-social { top: 372px; }
</style>
</head>
<body>
  <section class="business-card">
    <svg class="card-shapes" viewBox="0 0 1040 620" preserveAspectRatio="none" aria-hidden="true">
      <defs>
        <linearGradient id="lightFace" x1="0" y1="0" x2="1" y2="1">
          <stop offset="0" stop-color="var(--card-light-edge)"/>
          <stop offset="0.35" stop-color="var(--card-light)"/>
          <stop offset="1" stop-color="var(--card-light-edge)"/>
        </linearGradient>
        <linearGradient id="darkFace" x1="0" y1="0" x2="1" y2="1">
          <stop offset="0" stop-color="var(--panel-dark)"/>
          <stop offset="1" stop-color="var(--panel-dark-deep)"/>
        </linearGradient>
        <linearGradient id="redBand" x1="0" y1="0" x2="1" y2="0">
          <stop offset="0" stop-color="var(--accent-red)"/>
          <stop offset="1" stop-color="var(--accent-red-deep)"/>
        </linearGradient>
      </defs>
      <rect class="light-face" width="1040" height="620" fill="url(#lightFace)"/>
      <path class="dark-panel" d="M340 0 H1040 V470 Q820 440 610 462 Z" fill="url(#darkFace)"/>
      <path class="green-swoosh" d="M0 538 Q420 410 1040 458 V478 Q430 432 0 560 Z" fill="var(--accent-green)"/>
      <path class="dark-edge" d="M560 470 Q820 452 1040 480 V490 Q820 462 560 476 Z" fill="var(--panel-dark-deep)"/>
      <path class="red-band" d="M0 588 Q430 480 1040 500 V620 H0 Z" fill="url(#redBand)"/>
    </svg>

    <h1 class="brand-name">Tortilla Grove Market</h1>

    <ul class="contact-list">
      <li class="contact-item item-address">
        <p class="contact-text">2415 CALLOWAY BLVD<br>DUNDALK, MD 21222</p>
        <span class="contact-icon">
          <svg viewBox="0 0 24 24"><path d="M12 3 2 11.5h3V21h5v-6h4v6h5v-9.5h3z" fill="var(--icon-yellow)"/></svg>
        </span>
      </li>
      <li class="contact-item item-email">
        <p class="contact-text">@tortillagrovemarket</p>
        <span class="contact-icon">
          <svg viewBox="0 0 24 24"><rect x="2" y="5" width="20" height="14" fill="var(--icon-yellow)"/><path d="M2.5 5.5 12 13l9.5-7.5" fill="none" stroke="var(--panel-dark)" stroke-width="1.4"/></svg>
        </span>
      </li>
      <li class="contact-item item-phone">
        <p class="contact-text">+1 410-555-0143</p>
        <span class="contact-icon">
          <svg viewBox="0 0 24 24"><rect x="6" y="1.5" width="12" height="21" rx="2.5" fill="var(--icon-yellow)"/><rect x="8" y="4.5" width="8" height="13" fill="var(--panel-dark)"/><circle cx="12" cy="20" r="1" fill="var(--panel-dark)"/></svg>
        </span>
      </li>
      <li class="contact-item item-social">
        <p class="contact-text">Tortilla Grove Market</p>
        <span class="contact-icon">
          <svg viewBox="0 0 24 24"><rect x="6" y="6" width="12" height="12" fill="var(--icon-yellow)"/></svg>
        </span>
      </li>
    </ul>
  </section>
</body>
</html>
```